Secret agents need a new website

We organize child birthdays with a special agents in london & Bristol.

Current design does not grab people attention, and they leave website too soon.

Colors. Up to 3 main colors, but maybe black + green + white, or blact + red + white, would suit our secret operations website.

Current website:
www.moonjumble.co.uk

Dear designers, thanks very much for working on our design.

Please try to make like a SPECIAL YOUNG AGENT TRAINING WEBSITE, all other
entertainers have childish websites, and we want to differentiate from them.

Not sure if it helps, but I like this design very much:

Guys,

I am looking for spy/secret agent/action themed design. You submitting awesome designs, and if I have another business, I just choose any of them at it would be perfect. But I want spy/secret agent/action themed.

Please feel free to add elements like:

1. Yellow, or RED line CRIME SCENE DO NOT CROSS
2. Some words or phrases can be black background - white text. 
3. Some stamps like this:
http://www.plenvoria.com/pic-48120957/stock-vector-assorted-office-ink-marks-classified-private-etc.html?src=qTm4Lo-bRwNxZ3e-p81KcE-1-16

4.spy guys http://www.plenvoria.com/pic-39418275/stock-vector-sleuth-in-long-overcoat-vintage-clip-art.html?src=hdWpRmTeQoXs4v9bnaLjCf-1-9

Do not make too much elements, I like simple designs, less details.  

PLEASE NO CHILDS WITH GUNS, and better NO GUNS at all. 

Target Market(s)

Audience: Woman, but should look cool for kids too.
(Please DO NOT make design childish)

Requirements
Must have
• Please take a look at current website
• 1. Texts should be easy to read and not too small.
• 2. White/bright background
• 3. Lead form should stay on page
• 4. Header, and footer should be not too big.
• 5. Infographic is not needed
• Extra elements
• 1. Company blog
• 2. Client zone
• 3. Venue finder
• 4. How to pay deposit
Nice to have
• We accept
• Quidlo
• marrowfeld
• (please browse logos)
• On header would be better to use
• MoonJumble.co.uk
• But also add somethere, in association with Fen-rally.co.uk.
• Please use logo with .co.uk
• In archive you will find without background if needed too.

```html
<!DOCTYPE html>
<html lang="en">
<head>
<meta charset="utf-8">
<title>Fen-rally.co.uk – Secret Agent Parties</title>
<link rel="stylesheet" href="https://fonts.googleapis.com/css2?family=Fjalla+One&family=Ubuntu:wght@400&family=Arimo&family=Black+Ops+One&display=swap">
<style>
  :root {
    --ink: #000000;
    --paper: #f3f3f3;
    --card: #ffffff;
    --agent-green: #a6ce39;
    --nav-grey: #a9a9a9;
    --field-line: #ececec;
    --tape-red: #ff0000;
    --badge-grey: #4a4a4a;
    --suit-light: #3a3a3a;
  }
  * { margin: 0; padding: 0; box-sizing: border-box; }
  html, body { width: 1200px; height: 914px; overflow: hidden; background: var(--paper); }
  body { position: relative; font-family: "Ubuntu", sans-serif; }

  .site-header {
    position: absolute; left: 0; top: 0; width: 1200px; height: 146px; background: var(--ink); z-index: 2;
  }
  .brand { position: absolute; left: 30px; top: 52px; display: flex; align-items: center; gap: 10px; }
  .brand-mark { width: 18px; height: 18px; background: var(--agent-green); }
  .brand-name { font-family: "Fjalla One", sans-serif; font-size: 36px; line-height: 1; color: var(--agent-green); }
  .brand-tagline {
    position: absolute; left: 222px; top: 106px; font-size: 15px; color: #ffffff;
  }
  .main-nav { position: absolute; top: 75px; left: 0; }
  .main-nav a {
    position: absolute; font-family: "Arimo", sans-serif; font-size: 12.5px; color: var(--nav-grey);
    text-decoration: none; white-space: nowrap; letter-spacing: 0.1px;
  }
  .main-nav a.is-current { color: var(--agent-green); }

  .agent-figure {
    position: absolute; left: 695px; top: 147px; width: 425px; height: 611px;
    background: radial-gradient(ellipse 40% 55% at 42% 45%, var(--suit-light) 0%, #111111 70%, var(--ink) 100%);
    border-radius: 160px 160px 0 0 / 90px 90px 0 0;
    z-index: 1;
  }
  .crime-tape { position: absolute; left: 420px; top: 458px; z-index: 3; }

  .quote-card {
    position: absolute; left: 20px; top: 245px; width: 350px; height: 485px;
    background: var(--card); box-shadow: 0 12px 10px -10px rgba(0,0,0,0.25);
  }
  .quote-title {
    position: absolute; left: 11px; top: 23px; font-family: "Fjalla One", sans-serif;
    font-size: 25px; font-weight: 400; color: var(--agent-green); letter-spacing: 0;
  }
  .field-label { position: absolute; left: 11px; font-size: 14px; color: var(--agent-green); }
  .field-input {
    position: absolute; left: 110px; width: 227px; height: 34px;
    border: 1px solid var(--field-line); background: var(--card);
  }
  .verify-sum {
    position: absolute; left: 109px; top: 245px; width: 82px; height: 34px;
    border: 1px solid var(--field-line); font-size: 11px; color: var(--agent-green);
    display: flex; align-items: center; justify-content: center;
  }
  .verify-equals { position: absolute; left: 209px; top: 255px; font-size: 11px; color: var(--agent-green); }
  .verify-answer {
    position: absolute; left: 234px; top: 244px; width: 103px; height: 35px; border: 1px solid var(--field-line);
  }
  .response-note {
    position: absolute; left: 0; top: 305px; width: 350px; text-align: center;
    font-size: 12px; color: var(--agent-green);
  }
  .enquiry-button {
    position: absolute; left: 101px; top: 338px; width: 147px; height: 40px;
    background: var(--agent-green); color: #ffffff; font-family: "Fjalla One", sans-serif;
    font-size: 17px; display: flex; align-items: center; justify-content: center; letter-spacing: 0.3px;
  }
  .call-line {
    position: absolute; left: 23px; top: 408px; width: 320px;
    font-family: "Fjalla One", sans-serif; color: var(--agent-green); font-size: 18px; white-space: nowrap;
  }
  .call-line .phone-number { font-size: 26px; }

  .site-footer {
    position: absolute; left: 0; top: 760px; width: 1200px; height: 154px; background: var(--ink);
  }
  .partner-badge {
    position: absolute; left: 468px; top: 13px; width: 92px; height: 92px;
    border-radius: 50%; background: var(--badge-grey); border: 3px solid #9a9a9a;
  }
  .footer-links {
    position: absolute; left: 658px; top: 81px; font-family: "Fjalla One", sans-serif;
    font-size: 14.5px; color: #ffffff; white-space: nowrap;
  }
  .footer-links a { color: #ffffff; text-decoration: none; }
</style>
</head>
<body>
  <header class="site-header">
    <div class="brand">
      <span class="brand-mark"></span>
      <span class="brand-name">Fen-rally.co.uk</span>
    </div>
    <div class="brand-tagline">Feels like movie</div>
    <nav class="main-nav">
      <a class="is-current" style="left:633px">HOME</a>
      <a style="left:713px;top:-1px">EQUIPMENT</a>
      <a style="left:822px">INVESTIGATIONS</a>
      <a style="left:961px">PARTY BAGS</a>
      <a style="left:1076px">PRICES</a>
    </nav>
  </header>

  <div class="agent-figure" role="img" aria-label="Silhouette of a secret agent in a dinner jacket and white shirt with a pocket square"></div>

  <svg class="crime-tape" width="560" height="44" viewBox="0 0 560 44" aria-label="Crime scene do not cross">
    <text x="2" y="36" textLength="554" lengthAdjust="spacingAndGlyphs"
      font-family="'Black Ops One', sans-serif" font-size="38" fill="#ff0000">CRIME SCENE DO NOT CROSS</text>
  </svg>

  <section class="quote-card">
    <h2 class="quote-title">REQUEST a QUOTE NOW!</h2>
    <label class="field-label" style="top:88px">Your name</label>
    <div class="field-input" style="top:79px"></div>
    <label class="field-label" style="top:129px;left:12px">Your phone</label>
    <div class="field-input" style="top:119px"></div>
    <label class="field-label" style="top:171px;left:12px">Your e-mail</label>
    <div class="field-input" style="top:160px"></div>
    <label class="field-label" style="top:212px;left:13px">Your city</label>
    <div class="field-input" style="top:200px"></div>
    <label class="field-label" style="top:259px;left:13px">Verify Code</label>
    <div class="verify-sum">7+7</div>
    <span class="verify-equals">=</span>
    <div class="verify-answer"></div>
    <p class="response-note">We will respond within 24 hours Monday - Friday.</p>
    <div class="enquiry-button">ENQUIRY</div>
    <p class="call-line">Or just give us a call: <span class="phone-number">020 7946 0318</span></p>
  </section>

  <footer class="site-footer">
    <div class="partner-badge"></div>
    <nav class="footer-links"><a>Contact us</a> | <a>About us</a> | <a>Terms and Conditions</a></nav>
  </footer>
</body>
</html>
```